Real Estate Business card design

Company Name: Tamarind Holdings, LLC
subtitle: We pay cash for houses!
Daniel Whitcombe
Managing Director
555-214-0963
Dan@TamarindHoldingsLLC.example
www.TamarindHoldingsLLC.example

We pay referral fees for Seller and Buyer leads.

Back:
We offer referral fees for Seller and Buyer leads that close.

Please contact Hal at 555-214-0963 with your referrals or to learn more about the referral program!

I am open to different color options but I am going for a classic, elegant, clean, and professional look. Please use logo as a reference.

Target Market(s)

People selling their homes and people in the market for buying homes.

Contact Information for Business Card

please see project description

Font styles to use
Serif
Sans Serif
Script

Requirements
Must have
• must have my logo in it
Nice to have
• I like cards that are split down the middle but please come up with a few mock ups. Open to any color scheme.

```html
<!DOCTYPE html>
<html lang="en">
<head>
<meta charset="utf-8">
<title>Tamarind Holdings, LLC – Business Card</title>
<link rel="stylesheet" href="https://fonts.googleapis.com/css2?family=Oswald:wght@500&family=Roboto:wght@400;500;700&display=swap">
<style>
  :root {
    --backdrop: #141414;
    --card: #1c1c1c;
    --card-edge: #262626;
    --silver: #d4d4d4;
    --silver-soft: #b9b9b9;
    --silver-dim: #9a9a9a;
  }
  * { margin: 0; padding: 0; box-sizing: border-box; }
  html, body {
    width: 1200px; height: 900px; overflow: hidden;
    background: var(--backdrop);
    font-family: "Roboto", Arial, sans-serif;
    color: var(--silver);
  }
  .canvas {
    width: 1200px; height: 900px;
    display: flex; flex-direction: column; align-items: center; justify-content: center;
    gap: 40px;
  }
  .card {
    width: 660px; height: 377px;
    background: linear-gradient(135deg, var(--card) 0%, #202020 60%, #1a1a1a 100%);
    border: 1px solid var(--card-edge);
    box-shadow: 0 14px 30px rgba(0,0,0,.55);
    position: relative;
  }

  /* Front */
  .card-front {
    display: flex; flex-direction: column; align-items: center; justify-content: center;
  }
  .brand {
    display: flex; align-items: center; gap: 14px;
    margin-top: -10px;
  }
  .brand-mark {
    width: 18px; height: 18px; background: var(--silver);
  }
  .brand-name {
    font-weight: 500; font-size: 38px; color: var(--silver); letter-spacing: .5px;
  }
  .front-phone {
    margin-top: 42px;
    font-weight: 500; font-size: 22px; letter-spacing: 1px; color: var(--silver);
  }
  .front-note {
    margin-top: 8px;
    font-size: 13px; letter-spacing: .8px; text-transform: uppercase; color: var(--silver-soft);
  }

  /* Back */
  .card-back { padding: 0 60px; }
  .identity {
    position: absolute; top: 118px; left: 60px; right: 50px;
    display: flex; align-items: center;
  }
  .person { text-align: right; padding-right: 22px; }
  .person-name {
    font-family: "Oswald", "Arial Narrow", sans-serif;
    font-weight: 500; font-size: 34px; letter-spacing: 1.5px; text-transform: uppercase;
    color: var(--silver); line-height: 1.1;
  }
  .person-title { font-size: 15px; color: var(--silver-soft); margin-top: 2px; }
  .divider { width: 1px; height: 70px; background: var(--silver-dim); }
  .contacts { list-style: none; padding-left: 18px; }
  .contacts li {
    display: flex; align-items: center; gap: 7px;
    font-size: 15px; color: var(--silver); line-height: 1.45;
  }
  .contacts svg { width: 11px; height: 11px; flex: none; }
  .back-note {
    position: absolute; left: 60px; right: 40px; bottom: 80px;
    font-size: 20px; letter-spacing: .6px; text-transform: uppercase; color: var(--silver);
  }
</style>
</head>
<body>
<main class="canvas">
  <section class="card card-front">
    <div class="brand">
      <span class="brand-mark"></span>
      <span class="brand-name">Tamarind Holdings, LLC</span>
    </div>
    <p class="front-phone">555-214-0963</p>
    <p class="front-note">We offer referral fees for seller and buyer leads that close.</p>
  </section>

  <section class="card card-back">
    <div class="identity">
      <div class="person">
        <h1 class="person-name">Daniel Whitcombe</h1>
        <p class="person-title">Director</p>
      </div>
      <span class="divider"></span>
      <ul class="contacts">
        <li>
          <svg viewBox="0 0 12 12" aria-hidden="true"><path d="M2.5 1 L4.5 1 L5.2 3.6 L4 4.6 Q5 7 7.4 8 L8.4 6.8 L11 7.5 L11 9.5 Q10.5 11 9 11 Q1 10 1 3 Q1 1.5 2.5 1Z" fill="none" stroke="var(--silver)" stroke-width="1.1"/></svg>
          555-214-0963
        </li>
        <li>
          <svg viewBox="0 0 12 12" aria-hidden="true"><rect x="1" y="2.5" width="10" height="7" fill="none" stroke="var(--silver)" stroke-width="1.1"/><path d="M1 2.5 L6 6.5 L11 2.5" fill="none" stroke="var(--silver)" stroke-width="1.1"/></svg>
          Dan@TamarindHoldingsLLC.example
        </li>
        <li>
          <svg viewBox="0 0 12 12" aria-hidden="true"><circle cx="6" cy="6" r="5" fill="none" stroke="var(--silver)" stroke-width="1"/><ellipse cx="6" cy="6" rx="2.2" ry="5" fill="none" stroke="var(--silver)" stroke-width="1"/><path d="M1 6 H11" stroke="var(--silver)" stroke-width="1"/></svg>
          www.TamarindHoldingsLLC.example
        </li>
      </ul>
    </div>
    <p class="back-note">We pay referral fees for seller and buyer leads.</p>
  </section>
</main>
</body>
</html>
```